“The Future” Spring Fair Poster

We are putting together a school and community fair. We need a poster designed to advertise the event and give some important information to would be attendees. We’d like the poster graphics to evoke a minimalistic and futuristic aesthetic, be bold, yet fun! We will printing the posters, so we will need for them to be at high resolution and ready to send to print.

Target Market(s)

Students, Parents, and Community members

Industry/Entity Type

School

Font styles to use
Sans Serif

Colors
33a6d7
fabb78
9d9d9d
ffffff
1b1b1b
33b8a4

Requirements
Must have
• The Future
• Birch & Harbor Spring Fair 2018
• Friday, May 18th
• 5:00-9:00pm
• Tickets Will Be Available at Select Pick up & Drop Off Times
• Come Enjoy a Futuristic Evening of Food, Music, Entertainment, & Fun!
Nice to have
• We’d love to see a bold and graphic poster with a futuristic feel!
• See the sample image below from previous event poster and additional images for mood and inspiration. Would love to see metallics (silver or metallic colors)

```html
<!DOCTYPE html>
<html lang="en">
<head>
<meta charset="utf-8">
<title>The Future — Birch &amp; Harbor Spring Fair 2018</title>
<link href="https://fonts.googleapis.com/css2?family=Josefin+Sans:wght@600;700&family=Oswald:wght@600&family=Lora:ital@1&display=swap" rel="stylesheet">
<style>
  :root {
    --ink: #1b1b1b;
    --peach: #fabb78;
    --white: #ffffff;
    --teal-deep: #174a43;
    --teal: #266b62;
    --teal-light: #2f7d71;
  }
  html, body {
    margin: 0;
    padding: 0;
    overflow: hidden;
    background: var(--ink);
  }
  .poster {
    position: relative;
    width: 800px;
    height: 1200px;
    overflow: hidden;
    background: var(--ink);
  }
  .hero-photo {
    position: absolute;
    left: 0;
    top: 0;
    width: 340px;
    height: 1200px;
    background: linear-gradient(175deg, var(--teal-light) 0%, var(--teal) 50%, var(--teal-deep) 100%);
  }
  .event-title {
    margin: 0;
    font-family: "Oswald", sans-serif;
    font-weight: 600;
    font-size: 112px;
    letter-spacing: 2px;
    color: var(--white);
    text-transform: uppercase;
  }
  .event-title span {
    position: absolute;
    writing-mode: vertical-rl;
    line-height: 120px;
    white-space: nowrap;
  }
  .event-title .line-name { left: 166px; top: 62px; }
  .event-title .line-fair { left: 42px; top: 290px; }
  .details {
    position: absolute;
    left: 340px;
    top: 0;
    width: 460px;
    height: 1200px;
  }
  .theme {
    position: absolute;
    top: 80px;
    left: 0;
    width: 460px;
    margin: 0;
    text-align: center;
    font-family: "Josefin Sans", sans-serif;
    font-weight: 700;
    font-size: 31px;
    color: var(--white);
    text-transform: uppercase;
  }
  .rule {
    position: absolute;
    left: 53px;
    width: 358px;
    height: 5px;
    background: var(--peach);
  }
  .rule-top { top: 194px; }
  .rule-bottom { top: 857px; }
  .invite, .tickets {
    position: absolute;
    margin: 0;
    font-family: "Lora", serif;
    font-style: italic;
    font-size: 21px;
    line-height: 33px;
    color: var(--peach);
  }
  .invite { top: 316px; left: 57px; width: 345px; }
  .tickets { top: 976px; left: 75px; width: 325px; }
  .when {
    position: absolute;
    top: 492px;
    left: 0;
    width: 460px;
    margin: 0;
    text-align: center;
    font-family: "Josefin Sans", sans-serif;
    font-weight: 700;
    font-size: 33px;
    line-height: 47px;
    letter-spacing: 4px;
    color: var(--white);
  }
  .when span { display: block; }
  .ornament {
    position: absolute;
    top: 689px;
    width: 48px;
    height: 48px;
    background: radial-gradient(circle, rgba(250, 187, 120, 0.35) 0%, rgba(250, 187, 120, 0) 70%);
  }
  .ornament-left { left: 147px; }
  .ornament-right { left: 265px; }
  .accent {
    position: absolute;
    top: 0;
    left: 0;
  }
</style>
</head>
<body>
<main class="poster">
  <div class="hero-photo" role="img" aria-label="Photograph of teal geometric triangular architectural panels"></div>
  <h1 class="event-title">
    <span class="line-name">Birch and Harbor</span>
    <span class="line-fair">Spring Fair 2018</span>
  </h1>

  <section class="details">
    <h2 class="theme">The Future</h2>
    <div class="rule rule-top"></div>
    <p class="invite">come enjoy a futuristic evening of food, music, entertainment and fun!</p>
    <p class="when">
      <span>MAY 18,&nbsp; FRIDAY</span>
      <span>5:00 - 9:00 pm</span>
    </p>
    <div class="ornament ornament-left" role="img" aria-label="Small dotted diamond ornament"></div>
    <div class="ornament ornament-right" role="img" aria-label="Small dotted diamond ornament"></div>
    <div class="rule rule-bottom"></div>
    <p class="tickets">tickets will be available at select pick up and drop off times!</p>
  </section>

  <svg class="accent" width="800" height="1200" viewBox="0 0 800 1200" aria-hidden="true">
    <polygon fill="#fabb78" points="653,1200 709,1144 709,1107 757,1107 800,1063 800,1200"/>
  </svg>
</main>
</body>
</html>
```